Business Cards for Lean-In-Wise

I need a business card that uses elements of my color pallet and book along with my company name and logo. The primary thing I'd like to have stand out is the word Lean-In-Wise (i'd like to see this word in the orange from my pallet)
On the back of the card I want it to say Stop being Accountable, Be Lean-In-Wise

Contact Information for Business Card

Summit Hearthgroup logo, Lean-In-Wise, email - rtm@summithearthgroup.example, phone 555-208-4917, Harbor City | Lakeview

Requirements
Nice to have
• colors from my color pallet

```html
<!DOCTYPE html>
<html lang="en">
<head>
<meta charset="utf-8">
<title>Lean-In-Wise Business Cards</title>
<link href="https://fonts.googleapis.com/css2?family=Oswald:wght@600;700&family=Quicksand:wght@500&family=Roboto:wght@400&display=swap" rel="stylesheet">
<style>
  :root {
    --bg: #2b2b2d;
    --card: #ffffff;
    --orange: #ec5a24;
    --blue-dark: #1f4fa8;
    --blue: #2a8fd6;
    --ink: #222222;
  }
  * { margin: 0; padding: 0; box-sizing: border-box; }
  html, body { width: 1200px; height: 900px; overflow: hidden; background: var(--bg); }
  .canvas { position: relative; width: 1200px; height: 900px; }
  .card {
    position: absolute; left: 250px; width: 700px; height: 400px;
    background: var(--card); border-radius: 22px;
    box-shadow: 0 10px 30px rgba(0,0,0,.45);
    overflow: hidden;
  }
  .card-back { top: 36px; }
  .card-front { top: 464px; }

  .slogan {
    position: absolute; left: 0; right: 0; top: 130px; text-align: center;
    font-family: "Oswald", "Arial Narrow", sans-serif; font-weight: 700;
    color: var(--orange); text-transform: uppercase; line-height: 1; white-space: nowrap;
  }
  .slogan-lead { display: block; font-size: 42px; letter-spacing: .5px; }
  .slogan-main { display: block; font-size: 76px; margin-top: 8px; }

  .headline {
    position: absolute; left: 56px; top: 96px;
    font-family: "Oswald", "Arial Narrow", sans-serif; font-weight: 700;
    font-size: 56px; color: var(--orange); text-transform: uppercase; line-height: 1; white-space: nowrap;
  }

  .brand { position: absolute; right: 40px; top: 56px; width: 230px; text-align: center; }
  .brand-mark { display: block; margin: 0 auto 14px; }
  .brand-name {
    font-family: "Quicksand", sans-serif; font-weight: 500;
    font-size: 34px; line-height: 1.1; color: var(--blue-dark);
  }
  .brand-tagline {
    margin-top: 10px; font-family: "Quicksand", sans-serif; font-weight: 500;
    font-size: 15px; color: var(--blue-dark); white-space: nowrap;
  }

  .details { position: absolute; left: 56px; bottom: 46px; font-family: "Roboto", sans-serif; color: var(--ink); }
  .cities { list-style: none; margin-bottom: 22px; }
  .cities li { display: flex; align-items: center; gap: 12px; font-size: 18px; line-height: 1.3; }
  .cities li::before { content: ""; width: 9px; height: 9px; border-radius: 50%; background: var(--blue-dark); }
  .contact { list-style: none; }
  .contact li { display: flex; align-items: center; gap: 12px; font-size: 18px; line-height: 1.45; white-space: nowrap; }
  .contact svg { width: 16px; height: 16px; flex: none; }
  .contact .web-link { color: var(--ink); }
  .contact .web-link span { color: var(--blue-dark); }
</style>
</head>
<body>
<div class="canvas">

  <section class="card card-back">
    <p class="slogan">
      <span class="slogan-lead">Stop being Accountable,</span>
      <span class="slogan-main">Be Lean-In-Wise</span>
    </p>
  </section>

  <section class="card card-front">
    <h1 class="headline">Lean-In-Wise</h1>

    <div class="brand">
      <svg class="brand-mark" width="52" height="52" viewBox="0 0 56 56" aria-hidden="true">
        <circle cx="28" cy="28" r="26" fill="var(--blue)"/>
      </svg>
      <p class="brand-name">Summit Hearthgroup</p>
      <p class="brand-tagline">Every Business Grows Together!</p>
    </div>

    <div class="details">
      <ul class="cities">
        <li>Harbor City</li>
        <li>Lakeview</li>
      </ul>
      <ul class="contact">
        <li>
          <svg viewBox="0 0 24 24" aria-hidden="true"><path fill="var(--blue-dark)" d="M6.6 10.8a15.1 15.1 0 0 0 6.6 6.6l2.2-2.2a1 1 0 0 1 1-.25 11.4 11.4 0 0 0 3.6.57 1 1 0 0 1 1 1V20a1 1 0 0 1-1 1A17 17 0 0 1 3 4a1 1 0 0 1 1-1h3.5a1 1 0 0 1 1 1c0 1.25.2 2.45.57 3.570a1 1 0 0 1-.25 1z"/></svg>
          555-208-4917
        </li>
        <li>
          <svg viewBox="0 0 24 24" aria-hidden="true"><rect x="2.5" y="5" width="19" height="14" rx="1.5" fill="none" stroke="var(--blue-dark)" stroke-width="2"/><path d="M3 6l9 7 9-7" fill="none" stroke="var(--blue-dark)" stroke-width="2"/></svg>
          rtm@summithearthgroup.example
        </li>
        <li>
          <svg viewBox="0 0 24 24" aria-hidden="true"><circle cx="12" cy="12" r="9.5" fill="none" stroke="var(--blue-dark)" stroke-width="2"/><path d="M2.5 12h19M12 2.5c3 3 3 16 0 19M12 2.5c-3 3-3 16 0 19" fill="none" stroke="var(--blue-dark)" stroke-width="1.6"/></svg>
          <span class="web-link">www.<span>summithearthgroup</span>.example</span>
        </li>
      </ul>
    </div>
  </section>

</div>
</body>
</html>
```